Christmas Banner for frontpage of website

New online scarf store just opened needs a Christmas Banner stating Free Delivery (UK only). Also if it could incorporate guaranteed Christmas delivery if ordered before 18th (might be too wordy though?) I would really like it to bring some colour to the page. The page is currently black and white with a pink accent and is very simple which is why I would like something modern and elegant, simple but with some colour. It is a shopify store I understand the banner size should be 950px by 290px the website is www.velmorabay.co.uk

Target Market(s)

Ladies

Industry/Entity Type

Store

Requirements
Should not have
• Not to look tacky.

```html
<!DOCTYPE html>
<html lang="en">
<head>
<meta charset="utf-8">
<title>Merry Christmas – Free Delivery</title>
<link rel="stylesheet" href="https://fonts.googleapis.com/css2?family=Cookie&family=Josefin+Sans:wght@700&family=Crimson+Text&display=swap">
<style>
  :root {
    --wine-deep: #3e0610;
    --wine-dark: #5a0b1c;
    --wine-mid: #8e1235;
    --wine-glow: #c4245a;
    --ribbon-ink: #7a1530;
    --ribbon-tail: #e8cfd6;
    --snow: #ffffff;
    --sleigh: #8c1a30;
  }
  * { margin: 0; padding: 0; box-sizing: border-box; }
  html, body { width: 1200px; height: 366px; overflow: hidden; background: var(--wine-deep); }
  .banner {
    position: relative;
    width: 1200px;
    height: 366px;
    overflow: hidden;
    background:
      radial-gradient(ellipse 420px 300px at 620px 40px, rgba(230, 60, 120, 0.55), transparent 70%),
      radial-gradient(ellipse 700px 420px at 600px 120px, var(--wine-glow) 0%, var(--wine-mid) 35%, var(--wine-dark) 70%, var(--wine-deep) 100%);
    color: var(--snow);
  }
  .banner__art { position: absolute; inset: 0; }
  .sleigh-illustration {
    position: absolute; left: 101px; top: 76px; width: 190px; height: 57px;
    background: linear-gradient(90deg, rgba(140, 26, 48, 0.9), rgba(140, 26, 48, 0.6));
    border-radius: 20px;
  }
  .tree-illustration {
    position: absolute;
    background: linear-gradient(180deg, rgba(255,255,255,0.75), var(--snow));
    border-radius: 40% 40% 6px 6px;
  }
  .tree-illustration--left-large { left: 6px; top: 234px; width: 64px; height: 97px; }
  .tree-illustration--left-small { left: 76px; top: 275px; width: 44px; height: 63px; }
  .tree-illustration--right { left: 1111px; top: 202px; width: 70px; height: 129px; }

  .greeting {
    position: absolute; left: 0; right: 0; top: 20px;
    display: flex; align-items: center; justify-content: center; gap: 18px;
    font-family: "Cookie", cursive;
    font-size: 74px; line-height: 1;
  }
  .greeting__rule { width: 24px; height: 2px; background: var(--snow); margin-top: 8px; }
  .headline {
    position: absolute; left: 0; right: 0; top: 104px;
    text-align: center;
    font-family: "Josefin Sans", sans-serif; font-weight: 700;
    font-size: 70px; line-height: 1; letter-spacing: 1px;
  }
  .ribbon-label {
    position: absolute; left: 366px; width: 442px; top: 214px;
    text-align: center;
    font-family: "Crimson Text", serif;
    font-size: 31px; line-height: 1; letter-spacing: 0.5px;
    color: var(--ribbon-ink);
  }
  .delivery-note {
    position: absolute; left: 0; right: 0; top: 278px;
    text-align: center;
    font-family: "Crimson Text", serif;
    font-size: 14px; line-height: 19px; letter-spacing: 0.3px;
    text-transform: uppercase;
  }
</style>
</head>
<body>
<div class="banner">
  <svg class="banner__art" width="1200" height="366" viewBox="0 0 1200 366" aria-hidden="true">
    <!-- snow hills -->
    <path d="M0 335 Q120 330 215 366 L0 366 Z" fill="var(--snow)"/>
    <path d="M998 366 Q1080 318 1200 322 L1200 366 Z" fill="var(--snow)"/>
    <!-- ribbon tails -->
    <path d="M331 234 L379 240 L379 300 L331 309 L349 271 Z" fill="var(--ribbon-tail)" opacity="0.85"/>
    <path d="M869 234 L821 240 L821 300 L869 309 L851 271 Z" fill="var(--ribbon-tail)" opacity="0.85"/>
    <!-- ribbon band -->
    <path d="M366 189 Q587 212 808 189 L808 259 Q587 280 366 259 Z" fill="var(--snow)"/>
  </svg>

  <div class="sleigh-illustration" role="img" aria-label="Santa's sleigh pulled by reindeer flying across the sky"></div>
  <div class="tree-illustration tree-illustration--left-large" role="img" aria-label="Snowy fir tree"></div>
  <div class="tree-illustration tree-illustration--left-small" role="img" aria-label="Small snowy fir tree"></div>
  <div class="tree-illustration tree-illustration--right" role="img" aria-label="Snowy fir tree"></div>

  <div class="greeting"><span class="greeting__rule"></span><span class="greeting__word">Merry</span><span class="greeting__rule"></span></div>
  <h1 class="headline">CHRISTMAS</h1>
  <p class="ribbon-label">FREE DELIVERY (UK ONLY)</p>
  <p class="delivery-note">Guaranteed Christmas<br>Delivery if ordered before 18th</p>
</div>
</body>
</html>
```